Digital Album Cover - Where The Quiet River Bends (Piano & Cello)

HiI would like a digital album coverTitle: "Where The Quiet River Bends (Piano & Cello)"Artist: "Lorcan Pettigrew & The Oduya Priscilla"

• Original creativity
• Copyrighted images

```html
<!DOCTYPE html>
<html lang="en">
<head>
<meta charset="utf-8">
<title>Where the quiet river bends — Album Cover</title>
<link href="https://fonts.googleapis.com/css2?family=Gentium+Book+Plus:ital,wght@1,400&display=swap" rel="stylesheet">
<style>
  :root {
    --ink-navy: #0d1442;
    --deep-blue: #1f3f78;
    --steel-blue: #5d7fa8;
    --sky-pale: #dfeaf3;
    --gold: #d9ae62;
    --sand: #c9ad86;
    --mauve: #7a5a74;
    --glow: #fbf9f6;
  }
  html, body {
    margin: 0;
    padding: 0;
    width: 1200px;
    height: 1200px;
    overflow: hidden;
    background: var(--glow);
  }
  .cover {
    position: relative;
    width: 1200px;
    height: 1200px;
    overflow: hidden;
  }
  .cover-artwork {
    position: absolute;
    inset: 0;
    background:
      radial-gradient(ellipse 420px 360px at 980px 880px, var(--glow) 0%, rgba(251,249,246,0.9) 45%, rgba(251,249,246,0) 100%),
      radial-gradient(ellipse 360px 300px at 760px 160px, rgba(232,242,250,0.95) 0%, rgba(232,242,250,0) 100%),
      radial-gradient(ellipse 300px 260px at 1060px 120px, rgba(93,127,168,0.8) 0%, rgba(93,127,168,0) 100%),
      radial-gradient(ellipse 380px 320px at 140px 180px, rgba(31,63,120,0.9) 0%, rgba(31,63,120,0) 100%),
      radial-gradient(ellipse 300px 360px at 90px 760px, rgba(31,63,120,0.85) 0%, rgba(31,63,120,0) 100%),
      radial-gradient(ellipse 260px 200px at 330px 380px, rgba(217,174,98,0.85) 0%, rgba(217,174,98,0) 100%),
      radial-gradient(ellipse 320px 220px at 380px 620px, rgba(122,90,116,0.6) 0%, rgba(122,90,116,0) 100%),
      radial-gradient(ellipse 340px 280px at 360px 1050px, rgba(201,173,134,0.9) 0%, rgba(201,173,134,0) 100%),
      linear-gradient(135deg, var(--deep-blue) 0%, var(--steel-blue) 30%, var(--sand) 60%, var(--sky-pale) 100%);
  }
  .cover-text {
    position: absolute;
    left: 745px;
    top: 704px;
    width: 440px;
    color: var(--ink-navy);
    font-family: "Gentium Book Plus", Georgia, serif;
    font-style: italic;
  }
  .album-title {
    margin: 0;
    font-size: 80px;
    font-weight: 400;
    line-height: 80px;
    letter-spacing: -0.5px;
  }
  .album-artist {
    margin: 34px 0 0;
    font-size: 21px;
    font-weight: 400;
    line-height: 1.2;
  }
</style>
</head>
<body>
  <main class="cover">
    <div class="cover-artwork" role="img" aria-label="Abstract layered collage of fractured glass-like shards in deep blues, warm gold and mauve, fading into a soft white glow at the lower right"></div>
    <div class="cover-text">
      <h1 class="album-title">Where the quiet river bends</h1>
      <p class="album-artist">Lorcan Pettigrew &amp; The Oduya Priscilla"</p>
    </div>
  </main>
</body>
</html>
```